1200 x 150 pixel banner ad max size 200KB

Hi - I'm looking for an animated GIF to be used as an online digital banner advert.

The banner ad is to promote sales of gas cylinders from a world-leading manufacturer.

Headline 1: SLASH YOUR ADMINISTRATION COSTS BY 50%
Headline 2: If you're not happy with our service - we will give you your money back!
Headline 3 (if possible): FREE Regulator for all new customers/vessels

**The banner needs to really stand out of the page and reflect our company and brand - We exist to revolutionise ship safety, performance and crew welfare.**

The banner ad needs to include the product logo and company logo - both attached.

The blue colours in our logos are:
Dark Blue
Pantone 303
C100 M047 Y023 K079
R000 G031 B051
HTML 001F33

Light Blue
Pantone 2995
CO83 M001 Y000 K000
R080 G177 B234
HTML 05B1EA

Target Market(s)

Marine industry buyers - fleet managers, ship owners, technical purchasers, superintendants

Industry/Entity Type

Marine

Requirements
Must have
• Company colours, product and company logo

```html
<!DOCTYPE html>
<html lang="en">
<head>
<meta charset="utf-8">
<title>Brisktide Gas – Slash your administration costs</title>
<link rel="stylesheet" href="https://fonts.googleapis.com/css2?family=Open+Sans:wght@400;700&display=swap">
<style>
  :root {
    --navy: #001F33;
    --sky: #05B1EA;
    --band-light: #226c9c;
    --band-dark: #0c456f;
    --paper: #ffffff;
    --ink-light: #ffffff;
    --partner-blue: #0b4f8a;
  }
  html, body {
    margin: 0;
    padding: 0;
    overflow: hidden;
    background: var(--paper);
  }
  .banner {
    position: relative;
    width: 1200px;
    height: 150px;
    overflow: hidden;
    background: var(--paper);
    font-family: "Open Sans", Arial, sans-serif;
  }
  .band {
    position: absolute;
    inset: 0;
    width: 1200px;
    height: 150px;
  }
  .headline {
    position: absolute;
    left: 335px;
    width: 600px;
    top: 0;
    height: 150px;
    margin: 0;
    display: flex;
    align-items: center;
    justify-content: center;
    color: var(--ink-light);
    font-weight: 400;
    font-size: 19px;
    letter-spacing: 0.1px;
    white-space: nowrap;
  }
  .product-brand {
    position: absolute;
    left: 10px;
    top: 44px;
    display: flex;
    align-items: center;
    gap: 12px;
  }
  .product-brand__mark {
    width: 62px;
    height: 62px;
    border-radius: 12px;
    background: var(--sky);
  }
  .product-brand__name {
    color: var(--navy);
    font-weight: 700;
    font-size: 27px;
    white-space: nowrap;
  }
  .partner-brand {
    position: absolute;
    right: 24px;
    top: 0;
    height: 150px;
    display: flex;
    align-items: center;
    color: var(--partner-blue);
    font-weight: 700;
    font-size: 25px;
    white-space: nowrap;
  }
</style>
</head>
<body>
  <div class="banner">
    <svg class="band" viewBox="0 0 1200 150" aria-hidden="true">
      <defs>
        <linearGradient id="bandFill" x1="0" y1="0" x2="1" y2="0">
          <stop offset="0" stop-color="var(--band-light)"/>
          <stop offset="1" stop-color="var(--band-dark)"/>
        </linearGradient>
      </defs>
      <polygon points="295,0 870,0 975,150 375,150" fill="url(#bandFill)"/>
    </svg>

    <div class="product-brand">
      <span class="product-brand__mark"></span>
      <span class="product-brand__name">Brisktide Gas</span>
    </div>

    <h1 class="headline">SLASH YOUR ADMINISTRATION COSTS BY 50%</h1>

    <div class="partner-brand">Norvane Marine</div>
  </div>
</body>
</html>
```